Corporate Sheet Metal Santa claus card

We are looking for a great holiday business card to send out to clients and business associates. Looking for someone to design us a sheet metal santa claus. Attached is an example of a guy we had designed a few years back. Also attached are our company logos that I would like represented on the card too. Need a version for each company.

Industry/Entity Type

Construction

Font styles to use
Serif

Requirements
Must have
• Inside greeting:
• In warm appreciation of our association during the past year
• we extend our Best Wishes for a Joyous Holiday Season and a Successful New Year!

```html
<!DOCTYPE html>
<html lang="en">
<head>
<meta charset="utf-8">
<title>Happy Holidays – Norval Sheetmetal</title>
<link rel="stylesheet" href="https://fonts.googleapis.com/css2?family=Oswald:wght@500&family=Great+Vibes&display=swap">
<style>
  :root {
    --page-bg: #eef1f4;
    --card-light: #fbfbfb;
    --card-mid: #e4e4e4;
    --holiday-red: #b3121f;
    --script-red: #c8102e;
    --brand-blue: #1d4f91;
    --steel-dark: #5c5c62;
    --steel-light: #b9b9be;
    --star-white: #ffffff;
    --faint-grey: #c9c9c9;
    --art-silver: #e6e6e8;
    --art-red: #cf2a36;
  }
  * { margin: 0; padding: 0; box-sizing: border-box; }
  html, body { width: 1200px; height: 1000px; overflow: hidden; }
  body { background: var(--page-bg); position: relative; }

  .card {
    position: absolute;
    top: 170px;
    width: 460px;
    height: 640px;
    background: linear-gradient(135deg, var(--card-light) 0%, var(--card-mid) 55%, var(--card-light) 100%);
    box-shadow: 0 10px 30px rgba(0,0,0,0.12);
    overflow: hidden;
  }
  .card--front { left: 110px; }
  .card--inside { left: 630px; }

  .star { position: absolute; opacity: 0.9; }

  .front__title {
    position: absolute;
    top: 56px; left: 0; width: 100%;
    text-align: center;
    font-family: "Oswald", sans-serif;
    font-weight: 500;
    font-size: 54px;
    letter-spacing: 1px;
    color: var(--holiday-red);
    line-height: 1;
  }

  .front__artwork {
    position: absolute;
    left: 110px; top: 150px;
    width: 260px; height: 330px;
    background: linear-gradient(180deg, var(--art-silver) 0%, var(--art-red) 100%);
    opacity: 0.85;
  }

  .steel-band {
    position: absolute;
    left: 0; width: 100%;
    height: 120px;
    background: linear-gradient(180deg, var(--steel-light) 0%, #eaeaec 30%, var(--steel-dark) 62%, #d6d6d9 100%);
    display: flex; align-items: center; justify-content: center;
  }
  .card--front .steel-band { top: 480px; }
  .card--inside .steel-band { top: 28px; height: 110px; }

  .brand {
    display: flex; align-items: center; gap: 8px;
    font-family: "Oswald", sans-serif;
    font-weight: 500;
    font-size: 20px;
    letter-spacing: 2px;
    color: var(--brand-blue);
  }
  .brand__mark { width: 14px; height: 14px; background: var(--brand-blue); }

  .inside__message {
    position: absolute;
    top: 200px; left: 30px; right: 30px;
    text-align: center;
    font-family: "Great Vibes", cursive;
    font-size: 40px;
    line-height: 1.18;
    color: var(--script-red);
  }

  .inside__brand-faint {
    position: absolute;
    bottom: 46px; left: 0; width: 100%;
    text-align: center;
    font-family: "Oswald", sans-serif;
    font-weight: 500;
    font-size: 20px;
    letter-spacing: 2px;
    color: var(--faint-grey);
  }
</style>
</head>
<body>

<section class="card card--front">
  <svg class="star" style="left:380px;top:110px" width="50" height="50" viewBox="0 0 100 100"><polygon points="50,5 61,38 95,38 67,58 78,92 50,72 22,92 33,58 5,38 39,38" fill="var(--star-white)"/></svg>
  <svg class="star" style="left:50px;top:200px" width="42" height="42" viewBox="0 0 100 100"><polygon points="50,5 61,38 95,38 67,58 78,92 50,72 22,92 33,58 5,38 39,38" fill="var(--star-white)"/></svg>
  <svg class="star" style="left:60px;top:370px" width="40" height="40" viewBox="0 0 100 100"><polygon points="50,5 61,38 95,38 67,58 78,92 50,72 22,92 33,58 5,38 39,38" fill="var(--star-white)"/></svg>

  <h1 class="front__title">HAPPY HOLIDAYS</h1>
  <div class="front__artwork" role="img" aria-label="Holiday character illustration in red and brushed silver"></div>

  <div class="steel-band">
    <div class="brand"><span class="brand__mark"></span>NORVAL SHEETMETAL</div>
  </div>
</section>

<section class="card card--inside">
  <div class="steel-band">
    <div class="brand"><span class="brand__mark"></span>NORVAL SHEETMETAL</div>
  </div>

  <svg class="star" style="left:40px;top:170px" width="50" height="50" viewBox="0 0 100 100"><polygon points="50,5 61,38 95,38 67,58 78,92 50,72 22,92 33,58 5,38 39,38" fill="var(--star-white)"/></svg>
  <svg class="star" style="left:370px;top:190px" width="60" height="60" viewBox="0 0 100 100"><polygon points="50,5 61,38 95,38 67,58 78,92 50,72 22,92 33,58 5,38 39,38" fill="var(--star-white)"/></svg>
  <svg class="star" style="left:40px;top:440px" width="70" height="70" viewBox="0 0 100 100"><polygon points="50,5 61,38 95,38 67,58 78,92 50,72 22,92 33,58 5,38 39,38" fill="var(--star-white)"/></svg>
  <svg class="star" style="left:370px;top:500px" width="60" height="60" viewBox="0 0 100 100"><polygon points="50,5 61,38 95,38 67,58 78,92 50,72 22,92 33,58 5,38 39,38" fill="var(--star-white)"/></svg>

  <p class="inside__message">We extend our<br>Best Wishes for a<br>Joyous Holiday Season<br>and a<br>Successful New Year!</p>

  <div class="inside__brand-faint">NORVAL SHEETMETAL</div>
</section>

</body>
</html>
```